Velvetorchid Hair & Beauty Business Card

Velvetorchid Hair & Beauty is a boutique salon located in the picturesque Lake Taupo NZ. The salon is very luxurious, opulent gold gilded mirrors, chandelier lit, contemporary french decor, sets the mood to create beautiful hair, makeup and all beauty services. Just had a new logo design and now after a new business card.
Logo
14 Korowhai Street
Taupo
Phone (07) 548 6193
www.velvetorchid.co.nz
email hair@velvetorchid.co.nz
Marlena Swithin
Also need a space to put in Stylist name, date, appointment time. thanks;)
Another idea is we could incorporate the wallpaper in the back ground either on the back or front or use an ornate glided frame (around the edge of the card) like on my website where my brides photos flash.
Decided against the wall paper but at least you can see our colour theme for the salon.
Updates

Please check out my updated brief . Thanks :)

Target Market(s)

25-60 years plus, mainly mid age females , wanting the best possible service , high standard of workmanship and money not a problem.

Industry/Entity Type

Boutique

Requirements
Must have
• Gold and silver

```html
<!DOCTYPE html>
<html lang="en">
<head>
<meta charset="utf-8">
<title>Velvetorchid Hair &amp; Beauty – Business Card Options</title>
<link rel="stylesheet" href="https://fonts.googleapis.com/css2?family=Nunito+Sans:wght@400;800&amp;family=Questrial&amp;display=swap">
<style>
  :root {
    --pink: #f9c9cd;
    --black: #000000;
    --silver: #d4d6e0;
    --gold: #8c7a34;
    --gold-soft: #b9a65c;
    --grey-text: #6f6f6f;
    --rule-pink: #f1cdd3;
    --card-edge: #9a9a9a;
    --paper: #ffffff;
  }
  * { box-sizing: border-box; margin: 0; padding: 0; }
  html, body { width: 700px; height: 1200px; overflow: hidden; background: var(--paper); }
  body { position: relative; font-family: "Nunito Sans", sans-serif; color: var(--black); }

  .option-label {
    position: absolute; left: 150px; width: 115px; text-align: center;
    font-weight: 800; font-size: 15px; letter-spacing: 0.3px;
  }
  .card {
    position: absolute; width: 237px; height: 416px;
    background: var(--paper); border: 1px solid var(--card-edge); overflow: hidden;
  }
  .card--front { left: 89px; }
  .card--back { left: 351px; }

  /* front stripe bands */
  .stripe-band { position: absolute; left: 0; right: 0; height: 49px; }
  .stripe-band__pattern {
    position: absolute; left: 0; right: 0; height: 36px;
    background: repeating-linear-gradient(90deg, var(--pink) 0 25.5px, var(--black) 25.5px 42.5px);
  }
  .stripe-band__bar { position: absolute; left: 0; right: 0; height: 9px; background: var(--black); }
  .stripe-band__silver { position: absolute; left: 0; right: 0; height: 4px; background: var(--silver); }
  .stripe-band--top { top: 0; }
  .stripe-band--top .stripe-band__pattern { top: 0; }
  .stripe-band--top .stripe-band__bar { top: 36px; }
  .stripe-band--top .stripe-band__silver { top: 45px; }
  .stripe-band--bottom { bottom: 0; }
  .stripe-band--bottom .stripe-band__pattern { bottom: 0; }
  .stripe-band--bottom .stripe-band__bar { bottom: 36px; }
  .stripe-band--bottom .stripe-band__silver { bottom: 45px; }

  .brand {
    position: absolute; left: 0; right: 0; top: 196px; text-align: center;
    font-family: "Questrial", sans-serif; font-size: 19px; color: var(--grey-text); line-height: 1.3;
  }

  /* back edge bands */
  .edge { position: absolute; left: 0; right: 0; }
  .edge--top { top: 0; height: 13px; background: linear-gradient(var(--black) 0 8px, var(--silver) 8px 13px); }
  .edge--bottom { bottom: 0; height: 13px; background: linear-gradient(var(--silver) 0 5px, var(--black) 5px 13px); }

  .brand-small {
    position: absolute; left: 0; right: 0; text-align: center;
    font-family: "Questrial", sans-serif; font-size: 13px; color: var(--gold);
  }
  .person {
    position: absolute; left: 0; right: 0; text-align: center;
    font-weight: 800; font-size: 15px; letter-spacing: 0.2px;
  }
  .person__surname { color: var(--pink); }
  .contact {
    position: absolute; left: 0; right: 0; text-align: center;
    font-size: 12px; line-height: 17.3px;
  }
  .write-line { position: absolute; left: 48px; width: 144px; height: 1px; background: var(--rule-pink); }
  .field-label { position: absolute; left: 48px; font-size: 11px; }
</style>
</head>
<body>

  <!-- Option 1 -->
  <div class="option-label" style="top:59px;">OPTION 1</div>

  <section class="card card--front" style="top:96px;">
    <div class="stripe-band stripe-band--top"><div class="stripe-band__pattern"></div><div class="stripe-band__bar"></div><div class="stripe-band__silver"></div></div>
    <p class="brand">Velvetorchid<br>Hair &amp; Beauty</p>
    <div class="stripe-band stripe-band--bottom"><div class="stripe-band__pattern"></div><div class="stripe-band__bar"></div><div class="stripe-band__silver"></div></div>
  </section>

  <section class="card card--back" style="top:96px;">
    <div class="edge edge--top"></div>
    <p class="brand-small" style="top:74px;">Velvetorchid</p>
    <p class="person" style="top:123px;">MARLENA <span class="person__surname">SWITHIN</span></p>
    <div class="write-line" style="top:176px;"></div>
    <div class="write-line" style="top:199px;"></div>
    <div class="write-line" style="top:222px;"></div>
    <div class="write-line" style="top:245px;"></div>
    <div class="write-line" style="top:267px;"></div>
    <p class="contact" style="top:313px;">14 Korowhai Street Taupo<br>+07 548 6193<br>www.velvetorchid.co.nz<br>hair@velvetorchid.co.nz</p>
    <div class="edge edge--bottom"></div>
  </section>

  <!-- Option 2 -->
  <div class="option-label" style="top:648px;">OPTION 2</div>

  <section class="card card--front" style="top:689px;">
    <div class="stripe-band stripe-band--top"><div class="stripe-band__pattern"></div><div class="stripe-band__bar"></div><div class="stripe-band__silver"></div></div>
    <p class="brand">Velvetorchid<br>Hair &amp; Beauty</p>
    <div class="stripe-band stripe-band--bottom"><div class="stripe-band__pattern"></div><div class="stripe-band__bar"></div><div class="stripe-band__silver"></div></div>
  </section>

  <section class="card card--back" style="top:689px;">
    <div class="edge edge--top"></div>
    <p class="brand-small" style="top:50px;">Velvetorchid</p>
    <p class="person" style="top:96px;">MARLENA <span class="person__surname">SWITHIN</span></p>
    <p class="contact" style="top:136px;">14 Korowhai Street Taupo<br>+07 548 6193<br>www.velvetorchid.co.nz<br>hair@velvetorchid.co.nz</p>
    <span class="field-label" style="top:242px;">Stylist</span>
    <div class="write-line" style="top:258px;"></div>
    <div class="write-line" style="top:281px;"></div>
    <div class="write-line" style="top:303px;"></div>
    <span class="field-label" style="top:309px;">Date &amp; Time</span>
    <div class="write-line" style="top:326px;"></div>
    <div class="write-line" style="top:348px;"></div>
    <div class="write-line" style="top:370px;"></div>
    <div class="edge edge--bottom"></div>
  </section>

</body>
</html>
```